Bref créative
Brisk Haulage Web Page
Brisk Haulage
Energy
Energy services company in the business of storing, transporting and handling the logistics of oilfield liquids (water, brine, oil, etc.)
Looking for an elegant site - not too busy and distracting.
left side
see our logo and incorporate it.
Brisk Haulage Logo
Brisk Haulage Logo .gif

```html
<!DOCTYPE html>
<html lang="en">
<head>
<meta charset="utf-8">
<title>Brisk Haulage</title>
<link href="https://fonts.googleapis.com/css2?family=Arimo:wght@400;700&display=swap" rel="stylesheet">
<style>
:root{
  --page:#ffffff;
  --top-grey:#e4e6e9;
  --band-blue:#1f7fc6;
  --band-deep:#0f5f9e;
  --accent:#1d8fd6;
  --orange:#e8911f;
  --ink:#222629;
  --muted:#8a8f94;
  --line:#d6d9dc;
  --box:#f4f5f6;
}
*{margin:0;padding:0;box-sizing:border-box}
html,body{width:1200px;height:845px;overflow:hidden;background:var(--page);font-family:"Arimo",Arial,sans-serif;color:var(--ink)}
.canvas{position:relative;width:1200px;height:845px;background:linear-gradient(#dfe2e5 0,#f1f2f3 210px,#fff 210px)}
.blue-band{position:absolute;left:0;top:211px;width:1200px;height:270px;background:linear-gradient(var(--band-blue),var(--band-deep))}
.site{position:absolute;left:180px;top:18px;width:840px}
.header{height:150px;background:#fff;box-shadow:0 2px 6px rgba(0,0,0,.15);position:relative}
.brand{position:absolute;left:26px;top:44px;display:flex;align-items:center;gap:12px}
.brand-dot{width:34px;height:34px;border-radius:50%;background:var(--accent)}
.brand-name{font-size:30px;font-weight:700;color:var(--ink);letter-spacing:1px}
.phone{position:absolute;right:24px;top:16px;display:flex;align-items:center;gap:8px;color:var(--orange);font-size:15px;letter-spacing:.5px}
.nav{position:absolute;left:270px;right:14px;top:90px;height:34px;background:linear-gradient(#f7f8f9,#e9ebed);border:1px solid var(--line);display:flex;align-items:center;justify-content:space-around;font-size:11px;font-weight:700}
.nav a{color:var(--ink);text-decoration:none}
.nav a.current{color:var(--accent)}
.hero{position:relative;height:334px;background:linear-gradient(160deg,#c9cfd3 0%,#8fa4b6 35%,#3f6d97 60%,#1c3d5e 100%)}
.hero-caption{position:absolute;left:0;bottom:0;width:100%;height:48px;background:rgba(0,0,0,.82);padding:0 10px;display:flex;align-items:center;font-size:17px;font-weight:700;color:#fff;gap:6px}
.hero-caption span{color:#34a6ec}
.features{position:absolute;left:180px;top:540px;width:840px;display:flex;justify-content:space-between}
.feature{width:252px;height:156px;background:var(--box);border:1px solid var(--line);padding:12px 16px;position:relative}
.feature h2{font-size:20px;font-weight:400;color:var(--ink);margin-bottom:6px}
.feature p{font-size:10.5px;line-height:16px;color:var(--muted)}
.feature .more{position:absolute;right:14px;bottom:10px;font-size:10.5px;color:var(--ink);text-decoration:underline}
.feature.about{display:flex;gap:10px}
.feature.about .mark{width:48px;height:48px;border-radius:50%;background:var(--accent);margin-top:40px;flex:none}
.news{position:absolute;left:180px;top:715px;width:840px;height:40px;background:linear-gradient(#f7f8f9,#e9ebed);border:1px solid var(--line);display:flex;align-items:center;padding:0 16px;font-size:10px;color:var(--muted);gap:28px}
.news h3{font-size:15px;font-weight:400;color:#1c6ea8}
.news em{font-style:italic;margin-left:8px}
.news .all{margin-left:auto;color:var(--ink);text-decoration:underline}
.footer{position:absolute;left:0;top:798px;width:1200px;border-top:2px solid #bfc3c7;height:47px}
.footer p{position:absolute;left:190px;top:16px;font-size:10.5px;color:var(--ink)}
.social{position:absolute;right:182px;top:10px;display:flex;gap:8px}
.social span{width:24px;height:24px;border-radius:3px;background:#9aa3ab}
</style>
</head>
<body>
<div class="canvas">
  <div class="blue-band"></div>
  <div class="site">
    <header class="header">
      <div class="brand"><span class="brand-dot"></span><span class="brand-name">BRISK HAULAGE</span></div>
      <div class="phone">
        <svg width="20" height="14" viewBox="0 0 20 14"><path d="M1 5c0-3 4-4 9-4s9 1 9 4l-4 1-1-2H6L5 6 1 5z" fill="#222"/><rect x="5" y="7" width="10" height="7" rx="1" fill="#222"/></svg>
        CALL US: 5550142873
      </div>
      <nav class="nav">
        <a class="current">HOME</a><a>ABOUT US</a><a>OUR SERVICES</a><a>NEWS</a><a>LINKS</a><a>GALLERY</a><a>CONTACT</a>
      </nav>
    </header>
    <div class="hero" role="img" aria-label="Photograph of water cascading over a concrete weir">
      <div class="hero-caption">The team of experts and professionals <span>Water, Waste water and Energy Sector in your place</span></div>
    </div>
  </div>

  <section class="features">
    <article class="feature">
      <h2>Water Services</h2>
      <p>Lorem Ipsum is simply dummy text of the printing and typesetting industry. Lorem Ipsum has been the industry's standard dummy text ever since the 1500s, when an unknown printer</p>
      <a class="more">Learn More...</a>
    </article>
    <article class="feature">
      <h2>Energy</h2>
      <p>Lorem Ipsum is simply dummy text of the printing and typesetting industry. Lorem Ipsum has been the industry's standard dummy text ever since the 1500s, when an unknown printer</p>
      <a class="more">Learn More...</a>
    </article>
    <article class="feature about">
      <span class="mark"></span>
      <div>
        <h2>About us</h2>
        <p>Lorem Ipsum is simply dummy text of the printing and typesetting industry. Lorem Ipsum is simply dummy text of the printing and typesetting industry.</p>
      </div>
      <a class="more">Learn More...</a>
    </article>
  </section>

  <section class="news">
    <h3>News and events &#9656;</h3>
    <span>Lorem Ipsum is simply dummy text local we printer<em>May 07, 2011</em></span>
    <span>Lorem Ipsum is simply printed<em>May 07, 2011</em></span>
    <a class="all">View all</a>
  </section>

  <footer class="footer">
    <p>&copy; 2012 Brisk Haulage . All rights reserved</p>
    <div class="social"><span></span><span></span><span></span><span></span></div>
  </footer>
</div>
</body>
</html>
```